Web Design Nutrition supplements (Quilvara 5 pages)

We are looking for templates for a new nutrition supplement shop www.velomira.ch , targeting Swiss Female 65% /Male 35% over 40 yrs with high quality products (no performance enhancement /Body building products).
Our customers are not the most proficient in internet, so the website should be simple, easily understood. not too much web2.0 look and feel and functionality.

velomira.ch product offerings are high quality and supplied from top brands: like Dr. Holtfen, Varoun, talmquist, Nobrafit), for diets, weight management, antistress, anti-apathy, oligo-elements, omega-3 oils, and cosmetics.

We want the website design
1) to reflect our seriousness and expertise in the area,
2)to Inspire trust from our customers and address their needs in a personal and professional way (we answer your questions over email/Phone)
3) though we are not an pharmacy, our products are currently sold in pharmacies in Switzerland, so we want our customers to feel as well served online, as if they were in a pharmacy.
4) compare favorably to international websites (F, G) also selling online to Swiss customers: we are a truly Swiss company and can deliver within less than 18 h. in Switzerland (so the Swiss flag is an important design element for us)

We want to provide a superior buying experience,
1) important: providing sufficient product information: (intelligible snippet/summary of product info) should be visible on search result pages, and category pages,
2) clarity of design "emphasis" on products with clear call to action (buy)

Deliverables for the winning designer;
Photoshop files that can be easily be integrated in our quilvara shop.
- Homepage
- Category Page
- Product Page
For 1st evaluation and corrections of the proposals.

- Landing Page (for SEM Campaigns)
- Newsletter (Post finch)
as a second step.

Please use the attached wireframes, that should give you the exact content we want to provide (as well as functionality), the wireframes donnot define the user experience/design (it s more like a guidance, suggestion)

Target Market(s)

Swiss Males /35% Females 65% (both Swiss French/ Swiss German over 40 years

Industry/Entity Type

Nutrition

Requirements
Must have
• Deliverables:
- Homepage
- Category Page
- Product Page

- Newsletter template
- Landing Page

We attach:
- navigation to show how users can access the products (cat/ sub cat, but also search for body parts, objectives of healing... (see Kategorien-for-web.xls)
- Wireframes (myTrevolin)
- Logo (1 psd)
- Product images (zip files)
- Benchmarks: wellmorrow.co.uk (simplicity), kpv.com (expandable navigation),
- Competitors: ro7.de, talnori.com, talnori-deutschland.de, ultra-keen.eu

```html
<!DOCTYPE html>
<html lang="de">
<head>
<meta charset="utf-8">
<title>Velomira – Shop</title>
<link href="https://fonts.googleapis.com/css2?family=Oswald:wght@400;500&family=Arimo:wght@400;700&display=swap" rel="stylesheet">
<style>
:root{
  --green:#76b21c;
  --blue:#1a78c2;
  --slate:#5b7693;
  --btn:#6f8ea6;
  --nav:#2a2a2a;
  --footer:#363636;
  --footer-text:#9a9a9a;
  --footer-link:#3d8cc4;
  --line:#dcdcdc;
  --text:#444;
  --muted:#8a8a8a;
  --page:#fff;
}
*{box-sizing:border-box;margin:0;padding:0}
html,body{width:985px;height:1200px;overflow:hidden}
body{background:linear-gradient(#ececec,#f6f6f6 40%,#ececec);font-family:"Arimo",Arial,sans-serif;color:var(--text);font-size:10px;position:relative}
.page{position:absolute;left:100px;top:0;width:784px;height:1200px;background:var(--page)}
.abs{position:absolute}
a{color:inherit;text-decoration:none}

/* top bar */
.topbar{left:0;top:0;width:784px;height:27px;border-bottom:1px solid var(--line)}
.social-top{left:0;top:0;display:flex;height:26px}
.social-top span{width:31px;height:26px;border-right:1px solid var(--line);display:flex;align-items:center;justify-content:center}
.social-top span i{width:12px;height:12px;border-radius:50%;background:#8c8c8c;display:block}
.lang{right:160px;top:8px;display:flex;gap:8px}
.flag{width:16px;height:11px;display:flex}
.flag.de{flex-direction:column}
.flag b{flex:1;display:block}
.account{right:0;top:0;display:flex;height:26px;font-size:10px;color:var(--blue);white-space:nowrap}
.account a{padding:0 10px;border-left:1px solid var(--line);line-height:26px}

/* header */
.brand{left:16px;top:52px;display:flex;align-items:center;gap:10px}
.brand i{width:48px;height:48px;border-radius:50%;background:var(--green);display:block}
.brand span{font-family:"Arimo",Arial,sans-serif;font-size:40px;color:var(--slate);letter-spacing:-.5px}
.perk{top:42px;display:flex;align-items:flex-start;gap:6px;font-size:10px;line-height:13px;color:var(--green)}
.perk .ico{width:20px;height:20px;margin-top:2px}
.search{left:269px;top:92px;width:300px;height:23px;border:1px solid #c9c9c9;border-radius:2px;background:#f6f6f6;font-size:9.5px;color:#666;padding:5px 8px}
.search svg{position:absolute;right:6px;top:3px}
.cart{left:665px;top:40px;color:var(--blue);font-family:"Oswald",sans-serif;font-size:13px;display:flex;align-items:center;gap:8px}
.cart-sum{left:718px;top:62px;font-family:"Oswald",sans-serif;font-size:13px;color:#666}
.help{left:727px;top:99px;display:flex;align-items:center;gap:6px;color:var(--blue);font-size:10px}
.help i{width:13px;height:13px;border-radius:50%;background:#666;color:#fff;font-style:normal;font-size:9px;text-align:center;line-height:13px}

/* nav */
.mainnav{left:16px;top:131px;width:753px;height:37px;background:var(--nav);display:flex;justify-content:space-between;align-items:center;padding:0 12px}
.mainnav a{color:#fff;font-family:"Oswald",sans-serif;font-size:12.5px;font-weight:500;white-space:nowrap}
.crumb{left:16px;top:177px;width:753px;height:23px;background:#f0f0f0;border:1px solid #dedede;border-radius:3px;display:flex;align-items:center;gap:10px;padding-left:8px;font-size:9px;color:#666}

/* sidebar */
.box{border:1px solid #d8d8d8;background:#fff}
.sidebar{left:16px;top:213px;width:152px;height:227px;padding:12px 0 0 14px}
.sidebar li{list-style:none;font-size:10px;color:#777;height:23px;display:flex;align-items:center;gap:8px}
.sidebar li::before{content:"";width:4px;height:4px;border-radius:50%;background:#999}

/* hero */
.hero{left:181px;top:213px;width:423px;height:227px}
.hero h1{position:absolute;left:16px;top:20px;font-family:"Oswald",sans-serif;font-weight:500;font-size:30px;color:var(--green);line-height:1}
.hero h2{position:absolute;left:16px;top:61px;font-family:"Oswald",sans-serif;font-weight:400;font-size:18px;color:var(--green)}
.old{position:absolute;left:34px;top:112px;font-size:18px;color:#777;text-decoration:line-through}
.new{position:absolute;left:34px;top:141px;font-size:18px;color:var(--blue)}
.buy{position:absolute;left:26px;top:176px;width:78px;height:28px;background:var(--green);color:#fff;font-family:"Oswald",sans-serif;font-size:12px;display:flex;align-items:center;justify-content:center}
.hero .shot{position:absolute;left:252px;top:20px;width:140px;height:187px}

.support{left:616px;top:213px;width:153px;height:227px}
.support h3{text-align:center;font-family:"Oswald",sans-serif;font-weight:500;font-size:15px;color:#1f3f66;margin-top:10px}
.support .shot{position:absolute;left:8px;top:46px;width:135px;height:180px;border-radius:4px}

.shot{background:linear-gradient(160deg,#e8ecf2,#c7d0dc)}

/* specials */
.section-title{left:18px;top:461px;font-family:"Oswald",sans-serif;font-size:22px;color:var(--slate)}
.card{position:absolute;border:1px solid #d8d8d8;background:#fff}
.card.wide{top:501px;width:238px;height:146px}
.card.wide .shot{position:absolute;left:22px;top:18px;width:68px;height:108px;border-radius:6px}
.card.wide h4{position:absolute;left:113px;top:10px;font-weight:400;font-size:12px;color:var(--green)}
.card.wide p{position:absolute;left:113px;top:35px;width:112px;font-size:8.5px;line-height:12px;color:#999}
.card.wide .price{position:absolute;left:115px;top:74px}
.card.wide .cta{left:115px;top:102px}
.price{font-size:14px;color:#555}
.price b{color:var(--blue);font-weight:400}
.cta{position:absolute;width:87px;height:26px;background:var(--btn);color:#fff;font-size:9.5px;display:flex;align-items:center;justify-content:center}
.card.tall{top:663px;width:140px;height:230px}
.card.tall h4{position:absolute;left:0;right:0;top:10px;text-align:center;font-weight:400;font-size:11.5px;color:var(--green);white-space:nowrap}
.card.tall .shot{position:absolute;left:38px;top:38px;width:64px;height:112px;border-radius:6px}
.card.tall .price{position:absolute;left:0;right:0;top:164px;text-align:center}
.card.tall .cta{left:26px;top:191px}

/* footer */
.footer{left:0;top:917px;width:784px;height:283px;background:var(--footer)}
.footer .toplinks{position:absolute;left:20px;top:10px;font-size:9.5px;color:var(--footer-link)}
.footer .toplinks span{color:#777;margin:0 4px}
.footer .rule{position:absolute;left:0;top:31px;width:784px;height:1px;background:#2a2a2a;border-bottom:1px solid #444}
.footer h5{position:absolute;top:57px;font-family:"Oswald",sans-serif;font-weight:500;font-size:18px;color:var(--footer-text)}
.footer ul{position:absolute;top:96px;list-style:none}
.footer li{font-size:9.5px;color:var(--footer-link);height:23px}
.f-brand{position:absolute;right:22px;top:58px;display:flex;align-items:center;gap:8px}
.f-brand i{width:40px;height:40px;border-radius:50%;background:#8a8a8a;display:block}
.f-brand span{font-size:33px;color:#8a8a8a}
.phone{position:absolute;right:24px;top:130px;font-family:"Oswald",sans-serif;font-size:27px;color:#9a9a9a;white-space:nowrap}
.f-social{position:absolute;right:26px;top:190px;display:flex;gap:12px}
.f-social i{width:13px;height:13px;border-radius:50%;background:#8a8a8a;display:block}
.copy{position:absolute;left:0;right:0;top:254px;text-align:center;font-size:9.5px;color:#6f6f6f}
</style>
</head>
<body>
<div class="page">

  <div class="abs topbar">
    <div class="abs social-top"><span><i></i></span><span><i></i></span><span><i></i></span><span><i></i></span><span><i></i></span></div>
    <div class="abs lang">
      <span class="flag de"><b style="background:#111"></b><b style="background:#d22"></b><b style="background:#f5c400"></b></span>
      <span class="flag"><b style="background:#1f3f9a"></b><b style="background:#fff"></b><b style="background:#d22"></b></span>
    </div>
    <div class="abs account"><a href="#">Melden sie sich an</a><a href="#">Login</a></div>
  </div>

  <div class="abs brand"><i></i><span>velomira</span></div>

  <div class="abs perk" style="left:266px">
    <svg class="ico" viewBox="0 0 20 20"><rect x="1" y="5" width="11" height="8" fill="#666"/><path d="M12 8h4l3 3v2h-7z" fill="#666"/><circle cx="5" cy="15" r="2" fill="#666"/><circle cx="15" cy="15" r="2" fill="#666"/></svg>
    <div>18 Std. Lieferung<br>in der Schweiz</div>
  </div>
  <div class="abs perk" style="left:375px;top:38px">
    <svg class="ico" style="width:30px;height:30px" viewBox="0 0 30 30"><circle cx="15" cy="15" r="13" fill="none" stroke="#666" stroke-width="2"/><text x="15" y="14" font-size="7" text-anchor="middle" fill="#666" font-family="Arial">80</text><text x="15" y="21" font-size="6" text-anchor="middle" fill="#666" font-family="Arial">CHF</text></svg>
    <div style="margin-top:4px">Gratisversand ab<br>80 CHF</div>
  </div>
  <div class="abs perk" style="left:500px">
    <svg class="ico" viewBox="0 0 20 20"><path d="M10 2v16M4 5h12" stroke="#666" stroke-width="2" fill="none"/><circle cx="10" cy="10" r="3" fill="none" stroke="#666" stroke-width="1.5"/></svg>
    <div>Experten<br>Beratung</div>
  </div>

  <div class="abs search">Geben Sie einen Suchbegriff ein (z.B. Antioxidantien)
    <svg width="16" height="16" viewBox="0 0 16 16"><circle cx="6.5" cy="6.5" r="4.5" fill="none" stroke="#777" stroke-width="2"/><path d="M10 10l4 4" stroke="#777" stroke-width="2.5"/></svg>
  </div>

  <div class="abs cart"><svg width="14" height="12" viewBox="0 0 14 12"><path d="M0 1h3l2 7h7l2-5H4" fill="none" stroke="#444" stroke-width="1.6"/><circle cx="6" cy="10.5" r="1.3" fill="#444"/><circle cx="11" cy="10.5" r="1.3" fill="#444"/></svg>Zum Warenkorb</div>
  <div class="abs cart-sum">12.90 CHF</div>
  <div class="abs help"><i>?</i>Hilfe</div>

  <nav class="abs mainnav">
    <a href="#">Vitamins Mineralien</a><a href="#">Essentielle Fettsäure</a><a href="#">Prä-Probiotika</a><a href="#">Spirulina-Maca</a><a href="#">Gewichtabnahme</a><a href="#">Kosmetik</a><a href="#">Phytotherapie</a><a href="#">Funktionelle Nahrung</a><a href="#">ANGEBOTE</a>
  </nav>

  <div class="abs crumb">
    <svg width="14" height="12" viewBox="0 0 14 12"><path d="M7 0L0 6h2v6h4V8h2v4h4V6h2z" fill="#888"/></svg>
    <svg width="6" height="16" viewBox="0 0 6 16"><path d="M1 0l4 8-4 8" fill="none" stroke="#bbb"/></svg>
    This is a breadcrumb
  </div>

  <aside class="abs box sidebar">
    <ul><li>Probiotika</li><li>Probiotika</li><li>Lorem Ipsum</li><li>Lorem Ipsum</li><li>Dolor Sit Amet</li><li>Vestibulum Vena</li><li>Ipsum Dolor</li><li>Adipiscing Elit</li><li>Nullam Vitae</li></ul>
  </aside>

  <section class="abs box hero">
    <h1>Vitasport Elan</h1>
    <h2>Lorem Ipsum Dolor Sit Amet</h2>
    <div class="old">15.90 CHF</div>
    <div class="new">12.90 CHF</div>
    <a class="buy" href="#">Buy Now</a>
    <div class="shot" role="img" aria-label="Product box of Vitasport Elan" style="background:linear-gradient(160deg,#7b3f95 0 30%,#f4f4f6 30% 80%,#f2d23c 80%)"></div>
  </section>

  <section class="abs box support">
    <h3>Call Our Support Center</h3>
    <div class="shot" role="img" aria-label="Photo of a support agent with a headset"></div>
  </section>

  <h2 class="abs section-title">Weekly Specials</h2>

  <div class="card wide" style="left:16px">
    <div class="shot" role="img" aria-label="Tin of Basenpulver" style="background:linear-gradient(#4a6ea8 0 25%,#e9eef5 25%)"></div>
    <h4>Basenpulver</h4>
    <p>Lorem ipsum dolor sit amet, consectetur adipiscing elit. Etiam in pharetra nulla...</p>
    <div class="price"><b>8.50</b> CHF</div>
    <a class="cta" href="#">Add to cart</a>
  </div>
  <div class="card wide" style="left:274px">
    <div class="shot" role="img" aria-label="Tin of Miro-Café" style="background:linear-gradient(#c7261f,#9e1a15)"></div>
    <h4>Miro-Café</h4>
    <p>Lorem ipsum dolor sit amet, consectetur adipiscing elit. Etiam in pharetra nulla...</p>
    <div class="price"><b>8.50</b> CHF</div>
    <a class="cta" href="#">Add to cart</a>
  </div>
  <div class="card wide" style="left:531px">
    <div class="shot" role="img" aria-label="Bottle of Toravit" style="background:linear-gradient(#2f3f7a,#1e2a5a)"></div>
    <h4>Toravit</h4>
    <p>Lorem ipsum dolor sit amet, consectetur adipiscing elit. Etiam in pharetra nulla...</p>
    <div class="price"><b>8.50</b> CHF</div>
    <a class="cta" href="#">Add to cart</a>
  </div>

  <div class="card tall" style="left:16px">
    <h4>Selvacur</h4>
    <div class="shot" role="img" aria-label="Bottle of Selvacur" style="background:linear-gradient(#f2f2f2,#e8a35a 55%,#f2f2f2)"></div>
    <div class="price"><b>8.50</b> CHF</div>
    <a class="cta" href="#">Add to cart</a>
  </div>
  <div class="card tall" style="left:170px">
    <h4>Dolame</h4>
    <div class="shot" role="img" aria-label="Box of Dolame" style="background:linear-gradient(160deg,#f5f7fa,#cfe3f2)"></div>
    <div class="price"><b>8.50</b> CHF</div>
    <a class="cta" href="#">Add to cart</a>
  </div>
  <div class="card tall" style="left:323px">
    <h4>Vinol Synergie</h4>
    <div class="shot" role="img" aria-label="Bottle of Vinol Synergie" style="background:linear-gradient(#2c2f5a,#6b2a4a 55%,#2c2f5a)"></div>
    <div class="price"><b>8.50</b> CHF</div>
    <a class="cta" href="#">Add to cart</a>
  </div>
  <div class="card tall" style="left:477px">
    <h4>Granatapfel&nbsp; Elixier</h4>
    <div class="shot" role="img" aria-label="Bottle of Granatapfel Elixier" style="left:58px;width:24px;background:linear-gradient(#5a1a1c,#3a0f10)"></div>
    <div class="price"><b>8.50</b> CHF</div>
    <a class="cta" href="#">Add to cart</a>
  </div>
  <div class="card tall" style="left:630px">
    <h4>Melissen-Basentabletten</h4>
    <div class="shot" role="img" aria-label="Jar of Melissen-Basentabletten" style="background:linear-gradient(#2a3f6e,#dfe8f0 45%,#6f9ac0)"></div>
    <div class="price"><b>8.50</b> CHF</div>
    <a class="cta" href="#">Add to cart</a>
  </div>

  <footer class="abs footer">
    <div class="toplinks">Impressum<span>|</span>Wer Sind Wir<span>|</span>Über Uns<span>|</span>AGBs</div>
    <div class="rule"></div>
    <h5 style="left:27px">KUNDENSERVICE</h5>
    <ul style="left:27px"><li>Kontakt</li><li>Lexikon</li><li>Hilfe &amp; Antworten</li><li>Blog</li><li>Partnerprogramm</li><li>Reseller Programm</li></ul>
    <h5 style="left:212px">NAVIGATIONSHILFE</h5>
    <ul style="left:212px"><li>Suchbegriffe</li><li>Marken</li><li>Erweiterte Suche</li><li>Sitemap</li></ul>
    <ul style="left:399px"><li>Das Unternehmen</li><li>Expertise</li><li>Jobs</li><li>User Team</li></ul>
    <div class="f-brand"><i></i><span>velomira</span></div>
    <div class="phone">1-800-555-0199</div>
    <div class="f-social"><i></i><i></i><i></i><i></i><i></i></div>
    <div class="copy">Copyright © 2012 - Velomira&nbsp; -&nbsp; All Rights Reserved</div>
  </footer>

</div>
</body>
</html>
```